Bright Fern Landscape Services LLC
business cards, letterhead, and envelopes.
Bright Fern Landscape Services LLC -
Creative Brief
Simple
Lydia Harcourt
Owner
2187 NW 58th Ave. Ocala, Fl 34475
lharcourt@quillmesh.net
Would like to use my tagline somewhere not necessarily right under the logo.

```html
<!DOCTYPE html>
<html lang="en">
<head>
<meta charset="utf-8">
<title>Bright Fern Landscape Services LLC – Stationery</title>
<link href="https://fonts.googleapis.com/css2?family=Montserrat:wght@400;600;700&display=swap" rel="stylesheet">
<style>
  :root{
    --green:#5aa82a;
    --orange:#f39323;
    --ink:#555;
    --paper:#ffffff;
    --night:#111111;
    --ground:#efe9df;
    --tint:rgba(243,147,35,.10);
  }
  *{box-sizing:border-box;margin:0;padding:0}
  html,body{width:1200px;height:866px;overflow:hidden}
  body{background:var(--ground);font-family:"Montserrat",Arial,sans-serif;color:var(--ink);position:relative}
  .sheet{position:absolute;background:var(--paper);box-shadow:0 2px 6px rgba(0,0,0,.18);overflow:hidden}

  .brand{color:var(--green);font-weight:700;line-height:1.05}
  .brand small{display:block;font-size:.52em;letter-spacing:.04em;text-transform:uppercase}

  .band{position:absolute;left:0;right:0;background:var(--orange);color:#fff;
        font-size:7px;letter-spacing:.06em;text-transform:uppercase;padding-left:14px;display:flex;align-items:center;white-space:nowrap}
  .rule{position:absolute;left:0;right:0;height:2px;background:var(--green)}
  .contact{position:absolute;font-size:7px;line-height:1.7;white-space:nowrap}
  .contact .dot{display:inline-block;width:5px;height:5px;border-radius:50%;background:var(--green);margin-right:4px;vertical-align:middle}
  .faint{position:absolute;border-radius:50%;background:var(--tint)}

  /* letterhead */
  .letterhead{left:60px;top:108px;width:499px;height:696px}
  .letterhead .brand{position:absolute;left:28px;top:34px;font-size:26px}
  .letterhead .contact{left:28px;top:638px;font-size:7.5px}
  .letterhead .rule{top:670px}
  .letterhead .band{top:675px;height:14px}
  .letterhead .faint{right:30px;bottom:40px;width:130px;height:130px}

  /* business cards */
  .card{top:144px;width:216px;height:127px}
  .card-front{left:636px}
  .card-dark{left:876px;background:var(--night)}
  .card .brand{position:absolute;left:12px;top:14px;font-size:13px}
  .card .person{position:absolute;left:118px;top:50px;font-size:8.5px;color:var(--green);font-weight:600;white-space:nowrap}
  .card .person span{display:block;font-size:6px;color:var(--ink);font-weight:400}
  .card-dark .person span,.card-dark .contact{color:#ccc}
  .card .contact{left:12px;top:74px;font-size:5.5px}
  .card .rule{top:110px;height:1.5px}
  .card .band{top:113px;height:6px;padding:0}
  .card-dark .faint{right:12px;top:74px;width:30px;height:30px;background:rgba(255,255,255,.15)}

  /* envelopes */
  .envelope-back{left:581px;top:384px;width:554px;height:245px}
  .envelope-back svg{position:absolute;left:0;top:0}
  .envelope-front{left:504px;top:408px;width:564px;height:259px}
  .envelope-front .brand{position:absolute;left:22px;top:34px;font-size:24px}
  .envelope-front .contact{left:22px;top:196px;font-size:6.5px}
  .envelope-front .rule{top:228px}
  .envelope-front .band{top:233px;height:13px;font-size:6.5px}
  .envelope-front .faint{right:34px;top:80px;width:120px;height:120px}
</style>
</head>
<body>

<section class="sheet letterhead">
  <div class="brand">Bright Fern<small>Landscape Services LLC</small></div>
  <div class="faint"></div>
  <div class="contact">
    <div>2187 NW 58th Ave. Ocala, Fl 34475</div>
    <div><span class="dot"></span>(352) 555-0148 &nbsp; <span class="dot"></span>lharcourt@quillmesh.net</div>
  </div>
  <div class="rule"></div>
  <div class="band">Growing greener spaces with care every day</div>
</section>

<section class="sheet card card-front">
  <div class="brand">Bright Fern<small>Landscape Services LLC</small></div>
  <div class="person">Lydia Harcourt<span>Owner</span></div>
  <div class="contact">
    <div>2187 NW 58th Ave.</div>
    <div>Ocala, Fl 34475</div>
    <div><span class="dot"></span>(352) 555-0148</div>
    <div><span class="dot"></span>lharcourt@quillmesh.net</div>
  </div>
  <div class="rule"></div>
  <div class="band"></div>
</section>

<section class="sheet card card-dark">
  <div class="brand">Bright Fern<small>Landscape Services LLC</small></div>
  <div class="faint"></div>
  <div class="person">Lydia Harcourt<span>Owner</span></div>
  <div class="contact">
    <div>2187 NW 58th Ave.</div>
    <div>Ocala, Fl 34475</div>
    <div><span class="dot"></span>(352) 555-0148</div>
    <div><span class="dot"></span>lharcourt@quillmesh.net</div>
  </div>
  <div class="rule"></div>
  <div class="band"></div>
</section>

<section class="sheet envelope-back">
  <svg width="554" height="245" viewBox="0 0 554 245" aria-hidden="true">
    <path d="M0 0 H554 V18 C420 30 330 95 277 100 C224 95 134 30 0 18 Z" fill="var(--orange)"/>
  </svg>
</section>

<section class="sheet envelope-front">
  <div class="brand">Bright Fern<small>Landscape Services LLC</small></div>
  <div class="faint"></div>
  <div class="contact">
    <div>2187 NW 58th Ave. Ocala, Fl 34475</div>
    <div><span class="dot"></span>(352) 555-0148 &nbsp; <span class="dot"></span>lharcourt@quillmesh.net</div>
  </div>
  <div class="rule"></div>
  <div class="band">Growing greener spaces with care every day</div>
</section>

</body>
</html>
```